Testicular cancer awareness poster A4 size

We are a charity called Kestrelwind raising awareness of testicular cancer amongst young men. We would like a poster designed that can be displayed in Gyms and fitness centres. We would like it to be eye catching and have a slogan about checking yourself for signs of testicular cancer. It should include the Kestrelwind logo, website address and social media links. We want it to be fun and catchy and stand out in a gym. Something men will take notice of. Perhaps graphics relating to the gym environment (such as weights./dumbells) etc).

Target Market(s)

Young men aged 15-49 years of age

Industry/Entity Type

Charity

Requirements
Must have
• relevant graphic/s to be eye catching in a gym environment. Kestrelwind logo and website/social media information.
Nice to have
• A slogan/catchy phrase alerting men to check themselves for signs of testicular cancer.
Should not have
• Our website is www.kestrelwind.org.uk but we do not want a duplicate of images/style lifted from there please.

```html
<!DOCTYPE html>
<html lang="en">
<head>
<meta charset="utf-8">
<title>Kestrelwind – Touch yourself tonight</title>
<link rel="stylesheet" href="https://fonts.googleapis.com/css2?family=Arvo:wght@400;700&display=swap">
<style>
  :root {
    --page-bg: #e6e4e2;
    --poster-black: #050406;
    --window-light: rgba(120, 118, 124, 0.28);
    --skin-deep: #2a1c16;
    --skin-mid: #5a3f32;
    --skin-high: #7d5c4b;
    --tagline: #c7a597;
    --headline: #ffffff;
    --brand: #ffffff;
    --web-green: #b7d436;
    --social-blue: #2d6fb8;
  }
  html, body {
    margin: 0;
    width: 1200px;
    height: 900px;
    overflow: hidden;
    background: var(--page-bg);
  }
  .poster {
    position: absolute;
    left: 60px;
    top: 90px;
    width: 1080px;
    height: 720px;
    background: var(--poster-black);
    overflow: hidden;
    font-family: "Arvo", serif;
  }
  .window-light {
    position: absolute;
    left: 0;
    top: 0;
    width: 560px;
    height: 380px;
    background: linear-gradient(160deg, var(--window-light), rgba(0,0,0,0) 75%);
  }
  .athlete-photo {
    position: absolute;
    right: 0;
    top: 0;
    width: 540px;
    height: 720px;
    background:
      radial-gradient(ellipse 38% 45% at 52% 38%, var(--skin-high), var(--skin-mid) 45%, var(--skin-deep) 75%, rgba(5,4,6,0) 100%),
      var(--poster-black);
  }
  .tagline {
    position: absolute;
    left: 62px;
    top: 290px;
    margin: 0;
    width: 420px;
    font-weight: 400;
    font-size: 29px;
    line-height: 1.45;
    color: var(--tagline);
  }
  .headline {
    position: absolute;
    left: 62px;
    top: 425px;
    margin: 0;
    font-weight: 700;
    font-size: 46px;
    line-height: 1.4;
    color: var(--headline);
  }
  .brand {
    position: absolute;
    left: 62px;
    bottom: 48px;
  }
  .brand-name {
    font-weight: 700;
    font-size: 36px;
    color: var(--brand);
    line-height: 1;
  }
  .brand-web {
    margin-top: 10px;
    font-weight: 400;
    font-size: 17px;
    color: var(--web-green);
  }
  .social-links {
    position: absolute;
    right: 70px;
    bottom: 56px;
    display: flex;
    gap: 8px;
  }
  .social-square {
    width: 34px;
    height: 34px;
    background: var(--social-blue);
  }
</style>
</head>
<body>
  <main class="poster">
    <div class="window-light"></div>
    <div class="athlete-photo" role="img" aria-label="Photograph of a muscular, bare-chested man's torso, hands resting at his waist, lit against black"></div>

    <p class="tagline">A moment of awkwardness could save a lifetime.</p>
    <h1 class="headline">Touch yourself<br>tonight.</h1>

    <div class="brand">
      <div class="brand-name">Kestrelwind</div>
      <div class="brand-web">www.kestrelwind.org.uk</div>
    </div>

    <div class="social-links" aria-label="Social media">
      <span class="social-square"></span>
      <span class="social-square"></span>
      <span class="social-square"></span>
    </div>
  </main>
</body>
</html>
```